HiItsJonBrell.com needs a modern, eye-catching business card design

My name is Jon Brell and I own a video training (software development industry) website. I need a business card design that is eye catching for when I travel to conferences or do seminars. I would prefer something simple but bold. Something along the lines of this: https://pixvaultstatic.example/gallery_img/530172/44018/44018_9917302_530172_image.jpg

Note that I do not have a specific logo, but I do have an caricature I use on my site of myself. I've not attached it because I'm not really a fan of having it on my business cards. I would prefer lettering instead of an image. You can go to my website (https://hiitsjonbrell.com) for inspiration.

I want to add the following information on my card (the order of these, their size, and their casing is up to you):

Jon Brell
jon@HiItsJonBrell.com
@HiItsJonBrell
HiItsJonBrell.com
vidsharehub.example/HiItsJonBrell

I would also like to have somewhere on the card a small ad that says "Get a free course at https://HiItsJonBrell.com/FreeCourse". Feel free to play with that wording or layout if you need. I would prefer this text to be at the bottom of the card and subtle. Some small eye-catching thing might be ok but nothing huge or garish.

I plan on printing this card at pressquill.example (https://www.pressquill.example/us/design-guidelines/business-cards.html). I would like it to be the standard size (3.66" x 2.16"). I would prefer rounded corners and horizontal orientation. This is a two-side design. I would prefer the side with all of the information be primarily white but I like color text (again, flexible on that). On the front side, I like simple. Maybe just HiItsJonBrell.com (casing on that is up to you - whatever looks and reads the best - that goes for all of the casing). As for font choices, I prefer a modern, clean font. For example, Open Sans Light can be a nice option.

Website Info (might be helpful for the card):
Color Palette

Darkest blue - #263246
Alternate blue - #2F4E6A
Light blue - #2A98C3
Orange - #FF6201
White - #FFFFFF

Font for Jon Brell Logo

Jellyka Estryas Handwriting
http://www.typecrate.example/jellyka_estryas_handwriting.font

Fonts for Site Content and VidShare Thumbnails

Lovelo (bold title font)
http://www.glyphmill.example/lovelo-font/

Open Sans (body font)
http://www.letterbarn.example/fonts/open-sans

Industry/Entity Type

Software Development

Contact Information for Business Card

Jon Brell
jon@HiItsJonBrell.com
@HiItsJonBrell
HiItsJonBrell.com
vidsharehub.example/HiItsJonBrell

Get a free course at https://HiItsJonBrell.com/FreeCourse

Colors

Designer to choose colors to be used in the design.

Requirements
Nice to have
• Modern color - maybe primarily a color on the front and then that color as an accent on the back.
Should not have
• Lots of colors - I LOVE color but do not want a rainbow of colors on the card.

```html
<!DOCTYPE html>
<html lang="en">
<head>
<meta charset="utf-8">
<title>Jon Brell – Business Card</title>
<link rel="stylesheet" href="https://fonts.googleapis.com/css2?family=Open+Sans:wght@300;400;600&family=Josefin+Sans:wght@700&display=swap">
<style>
  :root {
    --bg: #e4e3e4;
    --blue-light: #2A98C3;
    --blue-deep: #125a7d;
    --ink: #263246;
    --text: #333a44;
    --orange: #FF6201;
    --orange-deep: #d95000;
    --white: #ffffff;
  }
  * { margin: 0; padding: 0; box-sizing: border-box; }
  html, body { width: 1200px; height: 1200px; overflow: hidden; }
  body {
    background: var(--bg);
    position: relative;
    font-family: "Open Sans", Arial, sans-serif;
  }
  .card {
    position: absolute;
    width: 785px;
    height: 464px;
    border-radius: 30px;
    overflow: hidden;
  }
  /* Front */
  .card--front {
    left: 94px; top: 153px;
    background: radial-gradient(ellipse 60% 65% at 50% 45%, var(--blue-light) 0%, #1f7ea8 55%, var(--blue-deep) 100%);
  }
  .front__name {
    position: absolute;
    left: 248px; top: 170px;
    color: var(--white);
    font-weight: 300;
    font-size: 64px;
    line-height: 1;
    letter-spacing: 1px;
  }
  .front__title {
    position: absolute;
    left: 248px; top: 272px;
    color: var(--white);
    font-family: "Josefin Sans", Arial, sans-serif;
    font-weight: 700;
    font-size: 17px;
    letter-spacing: 4.2px;
  }
  .front__band {
    position: absolute;
    left: 0; bottom: 0;
    width: 100%; height: 53px;
    background: linear-gradient(180deg, #f06507 0%, var(--orange-deep) 100%);
    color: var(--white);
    font-size: 17px;
    text-align: center;
    line-height: 48px;
  }
  /* Back */
  .card--back {
    left: 343px; top: 641px;
    height: 463px;
    background: var(--white);
  }
  .back__name {
    position: absolute;
    left: 145px; top: 190px;
    color: var(--ink);
    font-weight: 300;
    font-size: 54px;
    line-height: 1;
  }
  .back__contacts {
    position: absolute;
    left: 391px; top: 190px;
    list-style: none;
    color: var(--text);
    font-size: 17px;
    line-height: 24px;
  }
  .back__contacts li { display: flex; align-items: center; gap: 6px; }
  .back__contacts svg { flex: none; }
  .back__band {
    position: absolute;
    left: 0; top: 314px;
    width: 100%; height: 45px;
    background: linear-gradient(90deg, #f26a12 0%, var(--orange) 100%);
    color: var(--white);
    font-size: 18px;
    letter-spacing: 1px;
    text-align: center;
    line-height: 43px;
  }
</style>
</head>
<body>
  <section class="card card--front">
    <div class="front__name">Jon Brell</div>
    <div class="front__title">ONLINE TRAINER</div>
    <div class="front__band">"Get a free course at https://HiItsJonBrell.com/FreeCourse"</div>
  </section>

  <section class="card card--back">
    <div class="back__name">Jon Brell</div>
    <ul class="back__contacts">
      <li>
        <svg width="16" height="11" viewBox="0 0 16 11" aria-hidden="true"><rect width="16" height="11" rx="1" fill="var(--orange)"/><path d="M1 1 L8 6.5 L15 1" stroke="#fff" stroke-width="1.2" fill="none"/></svg>
        jon@HiItsJonBrell.com
      </li>
      <li>
        <svg width="16" height="11" viewBox="0 0 16 11" aria-hidden="true"><rect width="16" height="11" rx="1" fill="var(--orange)"/><path d="M1 1 L8 6.5 L15 1" stroke="#fff" stroke-width="1.2" fill="none"/></svg>
        @HiItsJonBrell
      </li>
      <li>
        <svg width="16" height="16" viewBox="0 0 16 16" aria-hidden="true"><circle cx="8" cy="8" r="7.5" fill="var(--orange)"/></svg>
        vidsharehub.example/HiItsJonBrell
      </li>
    </ul>
    <div class="back__band">www.HiItsJonBrell.com</div>
  </section>
</body>
</html>
```